Business card, Stationery and form for Crane Mill
Crane Mill, LLC an Energy Broker
Professional
Desmond Pilkerton
Principal
47 Birchway Lane
Lakewood, NJ 08539
(555) 214-KELP (5357)
dpilkerton@cranemill.com
www.cranemill.com
I will need to be able to change names etc on them for other workers.
Attached you will find a form that we use regularly (see the comment for the file).
I would also need the stationary designed in a way that is easy to use for word processing in MS Word, such as a template or in a word document that I can type on, besides in any way that may be printed.
I am guessing to use the secondary logo for the back but this is not required. An idea that I had but am unsure how it would look is to make that logo larger and then to place the words inside the lower grey area.
I may choose a full color design with pictures besides the more traditional one which I prefer in order to give the sales force a choice.
This is our primary logo
This is our secondary logo
This is a form which we use regularly. We primarily use the excel version here: http://cranemill.com/wp-content/uploads/2012/03/Crane-Mill-LOA-Form-unprotected.xlsx The form gets minor edits from time to time and I would prefer to have it designed as a header and footer or a template.

```html
<!DOCTYPE html>
<html lang="en">
<head>
<meta charset="utf-8">
<title>Crane Mill Stationery Concepts</title>
<link href="https://fonts.googleapis.com/css2?family=Montserrat:wght@700&family=Open+Sans:wght@400;600&display=swap" rel="stylesheet">
<style>
:root{
  --bg-deep:#173f48;
  --bg-mid:#24606b;
  --paper:#ffffff;
  --teal:#1f8fa8;
  --teal-light:#6fd3e6;
  --navy:#10324a;
  --ink:#2b3a44;
  --muted:#8aa3ad;
  --label:#cfe6ea;
}
*{box-sizing:border-box;margin:0;padding:0}
html,body{width:1200px;height:439px;overflow:hidden}
body{
  position:relative;
  background:radial-gradient(ellipse at 55% 45%,var(--bg-mid),var(--bg-deep) 75%);
  font-family:"Open Sans",sans-serif;color:var(--ink);
}
.sheet-title{position:absolute;left:26px;top:8px;font-size:9px;color:var(--label);letter-spacing:.3px}
.item-label{position:absolute;font-size:6px;color:var(--label);text-align:center}
.brand{display:flex;align-items:center;gap:3px;font-family:"Montserrat",sans-serif;font-weight:700;color:var(--navy);white-space:nowrap}
.brand .dot{border-radius:50%;background:var(--teal);flex:none}
.brand.light{color:var(--paper)}
.brand.light .dot{background:var(--teal-light)}

/* business cards */
.card{position:absolute;left:19px;width:101px;height:58px;box-shadow:0 2px 5px rgba(0,0,0,.45);overflow:hidden}
.card-front{top:28px;background:var(--paper);padding:5px}
.card-front .brand{font-size:6px}
.card-front .brand .dot{width:7px;height:7px}
.card-front .person{position:absolute;left:5px;top:30px;font-size:3.6px;line-height:1.35}
.card-front .person strong{font-size:4.2px;color:var(--navy)}
.card-front .contact{position:absolute;right:5px;top:30px;font-size:3.2px;line-height:1.45;text-align:left}
.card-front .band{position:absolute;left:0;right:0;bottom:0;height:4px;background:linear-gradient(90deg,var(--navy),var(--teal))}
.card-back-a{top:180px;height:79px;background:var(--paper);display:flex;flex-direction:column;align-items:center;justify-content:center;gap:6px}
.card-back-a .brand{font-size:9px}
.card-back-a .brand .dot{width:10px;height:10px}
.card-back-a .web{font-size:3.5px;color:var(--muted)}
.card-back-a .band{position:absolute;left:0;right:0;bottom:0;height:5px;background:linear-gradient(90deg,var(--navy),var(--teal))}
.card-back-b{top:300px;height:79px;background:radial-gradient(ellipse at 50% 40%,var(--teal-light),var(--teal) 45%,var(--navy));display:flex;align-items:center;justify-content:center}
.card-back-b .brand{font-size:9px}
.card-back-b .brand .dot{width:10px;height:10px}

/* letterheads */
.letterhead{position:absolute;top:19px;width:276px;height:384px;background:var(--paper);box-shadow:0 3px 8px rgba(0,0,0,.45);overflow:hidden}
.letterhead .brand{position:absolute;left:16px;top:14px;font-size:10px}
.letterhead .brand .dot{width:14px;height:14px}
.letterhead .contact{position:absolute;left:150px;top:14px;font-size:4.2px;line-height:1.5;color:var(--ink)}
.letterhead .mark{position:absolute;left:58px;top:95px;width:160px;height:160px;border-radius:50%;background:var(--teal);opacity:.08}
.letterhead svg{position:absolute;left:0;bottom:0}

/* envelopes */
.envelope{position:absolute;box-shadow:0 3px 7px rgba(0,0,0,.45);overflow:hidden}
.env-back{left:828px;top:19px;width:348px;height:100px;background:var(--paper)}
.env-back svg,.env-white svg{position:absolute;left:0;top:0}
.env-back .brand{position:absolute;left:154px;top:10px;font-size:6px}
.env-back .brand .dot{width:8px;height:8px}
.env-teal{left:838px;top:152px;width:300px;height:92px;background:radial-gradient(ellipse at 50% 30%,var(--teal-light),var(--teal) 50%,var(--navy));}
.env-teal .brand{position:absolute;left:122px;top:8px;font-size:6px}
.env-teal .brand .dot{width:8px;height:8px}
.env-white{background:var(--paper)}
.env-white .brand{position:absolute;left:8px;top:8px;font-size:6px}
.env-white .brand .dot{width:8px;height:8px}
.env-white .addr{position:absolute;left:8px;top:20px;font-size:3.4px;line-height:1.4}
.env-one{left:816px;top:236px;width:316px;height:96px}
.env-two{left:840px;top:298px;width:336px;height:104px}
</style>
</head>
<body>
<div class="sheet-title">Stationary Concepts</div>

<!-- business cards -->
<div class="card card-front">
  <div class="brand"><span class="dot"></span>Crane Mill, LLC</div>
  <div class="person"><strong>Desmond Pilkerton</strong><br>Principal</div>
  <div class="contact">(555) 214-KELP (5357)<br>dpilkerton@cranemill.com<br>www.cranemill.com<br>47 Birchway Lane</div>
  <div class="band"></div>
</div>
<div class="item-label" style="left:19px;top:92px;width:101px">Front Card Option A</div>

<div class="card card-back-a">
  <div class="brand"><span class="dot"></span>Crane Mill</div>
  <div class="web">www.cranemill.com</div>
  <div class="band"></div>
</div>
<div class="item-label" style="left:19px;top:264px;width:101px">Back Card Option A</div>

<div class="card card-back-b">
  <div class="brand light"><span class="dot"></span>Crane Mill</div>
</div>
<div class="item-label" style="left:19px;top:384px;width:101px">Back Card Option B</div>

<!-- letterheads -->
<div class="letterhead" style="left:197px">
  <div class="brand"><span class="dot"></span>Crane Mill, LLC</div>
  <div class="contact">47 Birchway Lane<br>Lakewood, NJ 08539<br>(555) 214-KELP (5357)<br>www.cranemill.com</div>
  <div class="mark"></div>
  <svg width="276" height="48" viewBox="0 0 276 48">
    <defs><linearGradient id="lhA" x1="0" x2="1"><stop offset="0" stop-color="#10324a"/><stop offset=".5" stop-color="#1f8fa8"/><stop offset="1" stop-color="#6fd3e6"/></linearGradient></defs>
    <path d="M0 22 Q140 6 276 18 L276 48 L0 48Z" fill="url(#lhA)"/>
    <path d="M0 20 Q140 2 276 14" stroke="#10324a" stroke-width="2" fill="none"/>
  </svg>
</div>
<div class="item-label" style="left:197px;top:408px;width:276px">Letterhead Option 1</div>

<div class="letterhead" style="left:504px">
  <div class="brand"><span class="dot"></span>Crane Mill, LLC</div>
  <div class="contact">47 Birchway Lane<br>Lakewood, NJ 08539<br>(555) 214-KELP (5357)<br>www.cranemill.com</div>
  <div class="mark"></div>
  <svg width="276" height="48" viewBox="0 0 276 48">
    <defs><linearGradient id="lhB" x1="0" x2="1"><stop offset="0" stop-color="#6fd3e6"/><stop offset=".5" stop-color="#1f8fa8"/><stop offset="1" stop-color="#10324a"/></linearGradient></defs>
    <path d="M0 18 Q136 4 276 22 L276 48 L0 48Z" fill="url(#lhB)"/>
    <path d="M0 14 Q136 0 276 20" stroke="#10324a" stroke-width="2" fill="none"/>
  </svg>
</div>
<div class="item-label" style="left:504px;top:408px;width:288px">Letterhead Option 2</div>

<!-- envelopes -->
<div class="envelope env-back">
  <svg width="348" height="100" viewBox="0 0 348 100">
    <path d="M0 0 H348 V20 Q174 58 0 20Z" fill="#0e1c24"/>
    <path d="M0 20 Q174 58 348 20" stroke="#1f8fa8" stroke-width="2" fill="none"/>
  </svg>
  <div class="brand light"><span class="dot"></span>Crane Mill</div>
</div>
<div class="envelope env-teal">
  <div class="brand light"><span class="dot"></span>Crane Mill</div>
</div>
<div class="envelope env-white env-one">
  <svg width="316" height="96" viewBox="0 0 316 96">
    <path d="M0 0 L158 52 L316 0" stroke="#d6e2e6" stroke-width="1" fill="none"/>
    <path d="M0 86 Q158 74 316 84 V96 H0Z" fill="#1f8fa8"/>
  </svg>
  <div class="brand"><span class="dot"></span>Crane Mill</div>
</div>
<div class="envelope env-white env-two">
  <svg width="336" height="104" viewBox="0 0 336 104">
    <path d="M0 92 Q168 78 336 90 V104 H0Z" fill="#1f8fa8"/>
    <path d="M0 90 Q168 75 336 87" stroke="#10324a" stroke-width="1.5" fill="none"/>
  </svg>
  <div class="brand"><span class="dot"></span>Crane Mill, LLC</div>
  <div class="addr">47 Birchway Lane<br>Lakewood, NJ 08539</div>
</div>
<div class="item-label" style="left:828px;top:408px;width:348px">Envelope Front/Back</div>
</body>
</html>
```